BRIGHTVALE MENTORING powerpoint deck.

I REQUIRE A COMPANY POWERPOINT SLIDE DECK, WHICH MAY ALSO INCLUDE A NUMBER OF "MODELS". THIS MAY ALSO REQUIRE SOME FOLLOW UP WORK.

ATTACHED IS AN EXAMPLE SLIDE DECK FOR ONE OF MY CLIENTS. I would like to see a mock up of a few slides and then i can send a complete deck over.

Please note my website... www.brightvalementoring.co.uk

I LOOK FORWARD TO SEEING YOUR DESIGN.

THANK YOU,

OWEN.

Target Market(s)

I work in the "learning and development"/ education/ leadership/ coaching industry

Industry/Entity Type

Leadership

Font styles to use
Other font styles liked:
• century gothic

Requirements
Must have
• ideally there would be some alignment to my website. www.brightvalementoring.co.uk
• be fresh, clean, simple enough. look professional.
Nice to have
• how you present "models" i would come back for more work in the future if the work is good.
Should not have
• too brash.

```html
<!DOCTYPE html>
<html lang="en">
<head>
<meta charset="utf-8">
<title>Brightvale Mentoring – Deck Concepts</title>
<link href="https://fonts.googleapis.com/css2?family=Arimo:wght@700&family=Carlito:wght@400;700&family=Didact+Gothic&display=swap" rel="stylesheet">
<style>
:root{
  --board:#3f1416;
  --board-title:#766a6a;
  --ink:#333333;
  --heading:#5f5f5f;
  --blue:#0a6cc4;
  --yellow:#ffc000;
  --green:#00b050;
  --grey:#6d6d6d;
  --light-grey:#a6a6a6;
  --olive:#8fba4e;
  --lime:#8ccf4d;
  --charcoal:#595959;
  --night:#333333;
  --sky:#00b0f0;
  --navy:#1f3d99;
  --red:#ff0000;
  --pie-yellow:#f2f200;
  --pie-teal:#24718f;
  --accent:#d9c84a;
}
*{margin:0;padding:0;box-sizing:border-box}
html,body{width:1200px;height:1200px;overflow:hidden;background:var(--board)}
.board{position:relative;width:1200px;height:1200px;background:var(--board)}
.board-title{position:absolute;top:50px;left:0;width:1200px;text-align:center;font-family:"Arimo",Arial,sans-serif;font-weight:700;font-size:33px;color:var(--board-title)}
.board-title span{border-bottom:2px solid var(--board-title);padding:0 0 2px}
.slide{position:absolute;background:#fff;display:block}
.slide-1{left:14px;top:160px}
.slide-2{left:607px;top:162px}
.slide-3{left:15px;top:498px}
.slide-4{left:607px;top:498px}
.slide-5{left:314px;top:838px}
.slide-title{font-family:"Carlito",Calibri,sans-serif;font-size:21px;fill:var(--heading)}
.body{font-family:"Didact Gothic","Century Gothic",sans-serif;fill:var(--ink)}
.tile-text{font-family:"Didact Gothic","Century Gothic",sans-serif;font-size:12.5px;fill:#fff;font-weight:700;text-anchor:middle}
.seg-label{font-family:"Didact Gothic",sans-serif;font-size:15px;fill:#fff}
.brand{font-family:"Didact Gothic",sans-serif;font-size:9px;fill:var(--ink);letter-spacing:.5px}
.finding{font-family:"Didact Gothic",sans-serif;font-size:9.3px;fill:#fff}
.finding-num{font-family:"Didact Gothic",sans-serif;font-size:23px;fill:#777;font-weight:700}
</style>
</head>
<body>
<div class="board">
  <h1 class="board-title"><span>PPT DESIGN IDEA - General Colors</span></h1>

  <!-- Slide 1: process model with call-outs -->
  <svg class="slide slide-1" width="584" height="328" viewBox="0 0 730 410">
    <defs>
      <path id="seg-01" d="M-107,0 A107,107 0 0 1 0,-107 L0,-47 A47,47 0 0 0 -47,0Z"/>
      <path id="seg-02" d="M0,-107 A107,107 0 0 1 107,0 L47,0 A47,47 0 0 0 0,-47Z"/>
      <path id="seg-03" d="M107,0 A107,107 0 0 1 0,107 L0,47 A47,47 0 0 0 47,0Z"/>
      <path id="seg-04" d="M0,107 A107,107 0 0 1 -107,0 L-47,0 A47,47 0 0 0 0,47Z"/>
      <g id="rule">
        <line x1="0" y1="0" x2="645" y2="0" stroke="#c8c8c8" stroke-width="3"/>
        <line x1="0" y1="0" x2="645" y2="0" stroke="#555" stroke-width="3" stroke-dasharray="20 23"/>
      </g>
      <g id="brand-mark">
        <circle cx="0" cy="0" r="9" fill="var(--accent)"/>
        <text class="brand" x="14" y="3">BRIGHTVALE MENTORING</text>
      </g>
      <marker id="arrow" viewBox="0 0 6 6" refX="5" refY="3" markerWidth="6" markerHeight="6" orient="auto"><path d="M0,0 L6,3 L0,6Z" fill="context-stroke"/></marker>
    </defs>
    <text class="slide-title" x="54" y="32">Example structure of Team coaching and</text>
    <text class="slide-title" x="54" y="58">Train the Team (TTT) sessions.</text>
    <use href="#brand-mark" x="565" y="34"/>
    <use href="#rule" x="43" y="64"/>

    <g transform="translate(360,220)">
      <g transform="rotate(20)" stroke="#fff" stroke-width="5">
        <use href="#seg-01" fill="var(--blue)"/>
        <use href="#seg-02" fill="var(--yellow)"/>
        <use href="#seg-03" fill="var(--green)"/>
        <use href="#seg-04" fill="var(--grey)"/>
      </g>
      <text class="seg-label" x="-58" y="-50">01</text>
      <text class="seg-label" x="54" y="-38">02</text>
      <text class="seg-label" x="38" y="64">03</text>
      <text class="seg-label" x="-72" y="48">04</text>
    </g>

    <g fill="none" stroke-width="1.2">
      <polyline points="288,150 288,130 218,130" stroke="#4aa3df" marker-end="url(#arrow)"/>
      <polyline points="436,150 436,130 508,130" stroke="var(--yellow)" marker-end="url(#arrow)"/>
      <polyline points="436,290 436,306 508,306" stroke="var(--green)" marker-end="url(#arrow)"/>
      <polyline points="288,290 288,306 218,306" stroke="#888" marker-end="url(#arrow)"/>
    </g>

    <rect x="54" y="86" width="163" height="87" fill="var(--blue)"/>
    <text class="body" font-size="12" fill="#fff" text-anchor="middle" style="fill:#fff"><tspan x="135" y="124">Regional manager and</tspan><tspan x="135" y="138">SMT involvement</tspan></text>

    <rect x="510" y="86" width="163" height="87" fill="var(--yellow)"/>
    <text class="body" font-size="12" text-anchor="middle" style="fill:#fff"><tspan x="592" y="111">Train the team. Present</tspan><tspan x="592" y="126">and provide content for</tspan><tspan x="592" y="140">the team to deliver to</tspan><tspan x="592" y="155">depot</tspan></text>

    <rect x="54" y="261" width="163" height="87" fill="var(--grey)"/>
    <text class="body" font-size="12" text-anchor="middle" style="fill:#fff"><tspan x="135" y="279">Team development</tspan><tspan x="135" y="294">element. (leadership</tspan><tspan x="135" y="308">development, peer</tspan><tspan x="135" y="323">assessment, PDP's and</tspan><tspan x="135" y="338">action learning)</tspan></text>

    <rect x="511" y="262" width="164" height="88" fill="var(--green)"/>
    <text class="body" font-size="12" text-anchor="middle" style="fill:#fff"><tspan x="593" y="286">Check in and coaching</tspan><tspan x="593" y="300">on core team</tspan><tspan x="593" y="315">objectives.</tspan><tspan x="593" y="330">Goals, RACI and what</tspan><tspan x="593" y="344">next.</tspan></text>

    <use href="#rule" x="43" y="373"/>
  </svg>

  <!-- Slide 2: process model with numbered list -->
  <svg class="slide slide-2" width="582" height="327" viewBox="0 0 727 409">
    <text class="slide-title" x="54" y="32">Example structure of Team coaching and</text>
    <text class="slide-title" x="54" y="58">Train the Team (TTT) sessions.</text>
    <use href="#brand-mark" x="565" y="34"/>
    <use href="#rule" x="43" y="64"/>
    <g transform="translate(213,213)">
      <g transform="rotate(20)" stroke="#fff" stroke-width="5">
        <use href="#seg-01" fill="var(--blue)"/>
        <use href="#seg-02" fill="var(--yellow)"/>
        <use href="#seg-03" fill="var(--green)"/>
        <use href="#seg-04" fill="var(--grey)"/>
      </g>
      <text class="seg-label" x="-58" y="-50">01</text>
      <text class="seg-label" x="54" y="-38">02</text>
      <text class="seg-label" x="38" y="64">03</text>
      <text class="seg-label" x="-72" y="48">04</text>
    </g>
    <line x1="347" y1="130" x2="347" y2="300" stroke="#bbb" stroke-dasharray="2 4"/>
    <g fill="#fff" stroke="#999" stroke-dasharray="2 2">
      <circle cx="386" cy="135" r="17"/><circle cx="386" cy="188" r="17"/>
      <circle cx="386" cy="237" r="17"/><circle cx="386" cy="293" r="17"/>
    </g>
    <g class="body" font-size="14" text-anchor="middle">
      <text x="386" y="140">01</text><text x="386" y="193">02</text>
      <text x="386" y="242">03</text><text x="386" y="298">04</text>
    </g>
    <g class="body" font-size="10">
      <text x="424" y="138" font-size="12">Regional manager and SMT involvement</text>
      <text><tspan x="422" y="185">Train the team. Present and provide content for</tspan><tspan x="422" y="198">the team to deliver to depot</tspan></text>
      <text><tspan x="422" y="234">Team development element.(leadership</tspan><tspan x="422" y="247">development, peer assessment, PDP's and</tspan><tspan x="422" y="260">action learning)</tspan></text>
      <text><tspan x="422" y="290">Check in and coaching on core team objectives.</tspan><tspan x="422" y="303">Goals, RACI and what next.</tspan></text>
    </g>
    <use href="#rule" x="43" y="373"/>
  </svg>

  <!-- Slide 3: pie chart -->
  <svg class="slide slide-3" width="582" height="328" viewBox="0 0 728 410">
    <defs>
      <linearGradient id="pie-side" x1="0" x2="1" y1="0" y2="0">
        <stop offset="0" stop-color="#e5e500"/><stop offset=".55" stop-color="#c9c900"/><stop offset="1" stop-color="#6b6a12"/>
      </linearGradient>
    </defs>
    <text class="slide-title" x="54" y="44">How we learn...</text>
    <use href="#brand-mark" x="565" y="34"/>
    <use href="#rule" x="43" y="64"/>
    <text x="338" y="127" text-anchor="middle" font-family="Carlito,Calibri,sans-serif" font-weight="700" font-size="16" fill="#111">Data Distribution</text>
    <path d="M161,201 A153,45 0 0 0 467,201 L467,236 A153,45 0 0 1 161,236 Z" fill="url(#pie-side)"/>
    <path d="M161,201 L161,236 A153,45 0 0 0 168,246 L168,215 Z" fill="#1b566d"/>
    <path d="M314,201 L314,156 A153,45 0 1 1 168.5,214.9 Z" fill="var(--pie-yellow)"/>
    <path d="M314,201 L168.5,214.9 A153,45 0 0 1 224,164.6 Z" fill="var(--pie-teal)"/>
    <path d="M314,201 L224,164.6 A153,45 0 0 1 314,156 Z" fill="#2b2b2b"/>
    <g font-family="Carlito,Calibri,sans-serif" font-size="13">
      <text x="408" y="228" fill="#222">70%</text>
      <text x="197" y="188" fill="#fff">20%</text>
      <text x="282" y="172" fill="#fff">10%</text>
    </g>
    <g font-family="Carlito,Calibri,sans-serif" font-size="14" fill="#111">
      <rect x="510" y="204" width="7" height="7" fill="var(--pie-yellow)"/><text x="520" y="213">Informal</text>
      <rect x="510" y="224" width="7" height="7" fill="var(--pie-teal)"/><text x="520" y="233">Others</text>
      <rect x="510" y="244" width="7" height="7" fill="#2b2b2b"/><text x="520" y="253">Formal</text>
    </g>
    <use href="#rule" x="43" y="373"/>
  </svg>

  <!-- Slide 4: topic tiles -->
  <svg class="slide slide-4" width="582" height="328" viewBox="0 0 727 410">
    <defs>
      <g id="stack-icon" fill="#fff">
        <path d="M4,0 H30 L34,5 H0Z"/><rect x="0" y="8" width="34" height="4"/><rect x="0" y="15" width="34" height="4"/>
      </g>
    </defs>
    <text class="slide-title" x="54" y="44">Train the trainer example topics*</text>
    <use href="#brand-mark" x="565" y="34"/>
    <use href="#rule" x="43" y="64"/>
    <text class="body" font-size="12"><tspan x="43" y="85">Sessions to be led by Ops Managers, Supers and Foremen. To create the right mindsets, behaviours and bring</tspan><tspan x="43" y="99">the Northgate way to life.</tspan></text>

    <g>
      <rect x="45" y="114" width="200" height="58" rx="4" fill="var(--olive)"/>
      <use href="#stack-icon" x="58" y="133"/>
      <text class="tile-text"><tspan x="168" y="132">The Northgate way</tspan><tspan x="168" y="147">values brought to</tspan><tspan x="168" y="162">life.</tspan></text>

      <rect x="264" y="114" width="200" height="58" rx="4" fill="#8c8c8c"/>
      <use href="#stack-icon" x="277" y="133"/>
      <text class="tile-text"><tspan x="387" y="132">Safety critical</tspan><tspan x="387" y="147">behaviours and</tspan><tspan x="387" y="162">initiatives.</tspan></text>

      <rect x="484" y="114" width="200" height="58" rx="4" fill="var(--yellow)"/>
      <use href="#stack-icon" x="497" y="133"/>
      <text class="tile-text"><tspan x="607" y="140">Leadership and how</tspan><tspan x="607" y="155">we do it around here.</tspan></text>

      <rect x="45" y="184" width="200" height="58" rx="4" fill="var(--blue)"/>
      <use href="#stack-icon" x="58" y="203"/>
      <text class="tile-text" x="168" y="217">Followership</text>

      <rect x="264" y="184" width="200" height="58" rx="4" fill="var(--lime)"/>
      <use href="#stack-icon" x="277" y="203"/>
      <text class="tile-text"><tspan x="387" y="210">Effective team work</tspan><tspan x="387" y="225">and communication</tspan></text>

      <rect x="484" y="184" width="200" height="58" rx="4" fill="var(--charcoal)"/>
      <use href="#stack-icon" x="497" y="203"/>
      <text class="tile-text"><tspan x="607" y="202">Feedback and</tspan><tspan x="607" y="217">courageous</tspan><tspan x="607" y="232">conversations</tspan></text>

      <rect x="45" y="253" width="200" height="58" rx="4" fill="var(--light-grey)"/>
      <use href="#stack-icon" x="58" y="272"/>
      <text class="tile-text"><tspan x="168" y="278">Inter team</tspan><tspan x="168" y="293">collaboration</tspan></text>

      <rect x="264" y="253" width="200" height="58" rx="4" fill="var(--night)"/>
      <use href="#stack-icon" x="277" y="272"/>
      <text class="tile-text"><tspan x="387" y="278">Resilience and well</tspan><tspan x="387" y="293">being</tspan></text>
    </g>

    <text class="body" font-size="11" x="43" y="336">* Sessions/ topics to be co-defined by Ops managers and BVM</text>
    <text class="body" font-size="8" x="43" y="362">(The Team are provided with slides, materials, games and team building activities, along with a trainer guide)</text>
    <use href="#rule" x="43" y="373"/>
  </svg>

  <!-- Slide 5: summary findings -->
  <svg class="slide slide-5" width="585" height="328" viewBox="0 0 731 410">
    <defs>
      <g id="finding-shape">
        <path d="M0,0 H271 V6 H0Z"/>
        <path d="M0,0 H240 L226,48 H0Z"/>
      </g>
    </defs>
    <text class="slide-title" x="54" y="45">Summary Findings</text>
    <use href="#brand-mark" x="590" y="36"/>
    <use href="#rule" x="43" y="64"/>

    <g>
      <use href="#finding-shape" x="65" y="94" fill="var(--light-grey)"/>
      <text class="finding"><tspan x="71" y="103">Develop a culture of empowerment. Freedom</tspan><tspan x="71" y="115">within a box. Shift from transactional managing</tspan><tspan x="71" y="127">to leading and coaching. Question marks on</tspan><tspan x="71" y="139">trust...</tspan></text>
      <text class="finding-num" x="303" y="131">01</text>

      <use href="#finding-shape" x="376" y="94" fill="var(--green)"/>
      <text class="finding"><tspan x="380" y="108">Forums for development: AM collaboration,</tspan><tspan x="380" y="120">share best practice and innovation in processes.</tspan><tspan x="380" y="132">Give them more of a voice and skin in the game.</tspan></text>
      <text class="finding-num" x="621" y="131">02</text>

      <use href="#finding-shape" x="65" y="160" fill="var(--sky)"/>
      <text class="finding"><tspan x="79" y="172">Development of fundamental skills in</tspan><tspan x="79" y="184">leadership, communication, planning and</tspan><tspan x="79" y="196">effective coaching skills are required.</tspan></text>
      <text class="finding-num" x="303" y="197">03</text>

      <use href="#finding-shape" x="376" y="160" fill="#404040"/>
      <text class="finding"><tspan x="380" y="170">Bring the values to life in their own way in depot</tspan><tspan x="380" y="182">(with enough consistency). Empower them to do it</tspan><tspan x="380" y="194">and create their own depot culture, the Northgate</tspan><tspan x="380" y="206">way.</tspan></text>
      <text class="finding-num" x="621" y="197">04</text>

      <use href="#finding-shape" x="65" y="226" fill="var(--yellow)"/>
      <text class="finding"><tspan x="79" y="244">SMT to mentor AM's and get closer. AM's</tspan><tspan x="79" y="256">question SMT visability.</tspan></text>
      <text class="finding-num" x="303" y="263">05</text>

      <use href="#finding-shape" x="376" y="226" fill="var(--navy)"/>
      <text class="finding"><tspan x="389" y="242">Use of KPI's and setting depot and</tspan><tspan x="389" y="254">organisational goals. Depots to have a line of</tspan><tspan x="389" y="266">sight to the bigger picture.</tspan></text>
      <text class="finding-num" x="621" y="263">06</text>

      <use href="#finding-shape" x="65" y="292" fill="var(--red)"/>
      <text class="finding"><tspan x="79" y="312">Develop a culture of feedback and coaching</tspan><tspan x="79" y="324">lead by AM's.</tspan></text>
      <text class="finding-num" x="303" y="329">07</text>

      <use href="#finding-shape" x="376" y="289" fill="var(--light-grey)"/>
      <text class="finding"><tspan x="391" y="310">Consistency of SOPs across depots and</tspan><tspan x="391" y="322">alignment of ways of working (forums).</tspan></text>
      <text class="finding-num" x="621" y="326">08</text>
    </g>

    <use href="#rule" x="43" y="373"/>
  </svg>
</div>
</body>
</html>
```